Managed IT services business card design

We haven't needed a business card since the founding of the business in 2005. All our clients have been coming through word of mouth. And lately more and more existing clients are requesting for our business cards to pass on to their contacts in recommending us.
So we needing a business card design. We use various innovative solutions and methodologies to provide IT services to small businesses in managing their IT systems. Our role is the same as an in-house, full-time IT Manager for our clients, but outsourced. So we take care of all our clients' IT needs, just as an IT Manager would be expected to perform.
We have a holding website, which we're happy to leave for now. If we can use the same logo would be great - www.lomvex.com.au
Preferred colours are shades of are white, grey and black.
We pride our business with the following traits: proactive, good service, prompt response, trustworthy.
Target Market(s)
Small businesses of any industry
Industry/Entity Type
Business

```html
<!DOCTYPE html>
<html lang="en">
<head>
<meta charset="utf-8">
<title>Lomvex Business Card</title>
<link rel="stylesheet" href="https://fonts.googleapis.com/css2?family=Cinzel:wght@400;500&display=swap">
<style>
  :root {
    --backdrop: #e4e4e4;
    --card-white: #ffffff;
    --band-grey: #b0b0b0;
    --charcoal: #3a3a3a;
    --logo-ink: #2f2f2f;
    --text-light: #f2f2f2;
  }
  * { margin: 0; padding: 0; box-sizing: border-box; }
  html, body {
    width: 1200px;
    height: 901px;
    overflow: hidden;
    background: var(--backdrop);
  }
  .business-card {
    position: absolute;
    left: 100px;
    top: 165px;
    width: 1000px;
    height: 571px;
    border-radius: 50px;
    overflow: hidden;
    background: var(--charcoal);
    box-shadow: 0 14px 40px rgba(0,0,0,0.18);
    font-family: "Cinzel", Georgia, serif;
  }
  .card-waves {
    position: absolute;
    inset: 0;
    width: 1000px;
    height: 571px;
  }
  .brand-name {
    position: absolute;
    left: 330px;
    top: 70px;
    font-size: 84px;
    font-weight: 400;
    letter-spacing: 12px;
    text-transform: lowercase;
    color: var(--logo-ink);
    line-height: 1;
  }
  .contact-list {
    position: absolute;
    left: 70px;
    top: 300px;
    list-style: none;
    color: var(--text-light);
    font-size: 17px;
    line-height: 25px;
  }
  .contact-item {
    display: flex;
    align-items: flex-start;
    gap: 9px;
  }
  .contact-icon {
    flex: none;
    width: 15px;
    height: 15px;
    margin-top: 4px;
  }
  .card-holder {
    position: absolute;
    right: 60px;
    bottom: 44px;
    text-align: right;
    color: var(--text-light);
  }
  .holder-name {
    font-size: 28px;
    line-height: 34px;
  }
  .holder-role {
    font-size: 24px;
    line-height: 30px;
  }
</style>
</head>
<body>
  <div class="business-card">
    <svg class="card-waves" viewBox="0 0 1000 571" aria-hidden="true">
      <path fill="var(--band-grey)" d="M0,0 L1000,0 L1000,408 C450,418 120,318 0,88 Z"/>
      <path fill="var(--charcoal)" d="M0,0 L1000,0 L1000,400 C450,410 120,310 0,80 Z"/>
      <path fill="var(--band-grey)" d="M0,0 L1000,0 L1000,390 C450,400 120,300 0,70 Z"/>
      <path fill="var(--card-white)" d="M0,0 L1000,0 L1000,350 C450,360 120,260 0,30 Z"/>
    </svg>

    <div class="brand-name">lomvex</div>

    <ul class="contact-list">
      <li class="contact-item">
        <svg class="contact-icon" viewBox="0 0 16 16"><circle cx="8" cy="8" r="8" fill="var(--text-light)"/><path d="M8 3.5a3 3 0 0 0-3 3c0 2.2 3 5.5 3 5.5s3-3.3 3-5.5a3 3 0 0 0-3-3z" fill="var(--charcoal)"/></svg>
        <span>Suite # 410, Kerr House,<br>NY 82917</span>
      </li>
      <li class="contact-item">
        <svg class="contact-icon" viewBox="0 0 16 16"><circle cx="8" cy="8" r="8" fill="var(--text-light)"/><path d="M5 4.5l1.6-.5 1 2.2-1 .8a5 5 0 0 0 2.4 2.4l.8-1 2.2 1-.5 1.6c-3.5 0-6.5-3-6.5-6.5z" fill="var(--charcoal)"/></svg>
        <span>213-555-0147</span>
      </li>
      <li class="contact-item">
        <svg class="contact-icon" viewBox="0 0 16 16"><circle cx="8" cy="8" r="8" fill="var(--text-light)"/><path d="M5 4.5l1.6-.5 1 2.2-1 .8a5 5 0 0 0 2.4 2.4l.8-1 2.2 1-.5 1.6c-3.5 0-6.5-3-6.5-6.5z" fill="var(--charcoal)"/></svg>
        <span>213-555-0192</span>
      </li>
      <li class="contact-item">
        <svg class="contact-icon" viewBox="0 0 16 16"><circle cx="8" cy="8" r="8" fill="var(--text-light)"/><path d="M5 4.5l1.6-.5 1 2.2-1 .8a5 5 0 0 0 2.4 2.4l.8-1 2.2 1-.5 1.6c-3.5 0-6.5-3-6.5-6.5z" fill="var(--charcoal)"/></svg>
        <span>213-555-0168</span>
      </li>
      <li class="contact-item">
        <svg class="contact-icon" viewBox="0 0 16 16"><circle cx="8" cy="8" r="8" fill="var(--text-light)"/><rect x="4" y="5" width="8" height="6" fill="none" stroke="var(--charcoal)" stroke-width="1.2"/><path d="M4 5l4 3.2L12 5" fill="none" stroke="var(--charcoal)" stroke-width="1.2"/></svg>
        <span>hello@lomvex.com.au</span>
      </li>
      <li class="contact-item">
        <svg class="contact-icon" viewBox="0 0 16 16"><circle cx="8" cy="8" r="8" fill="var(--text-light)"/><circle cx="8" cy="8" r="4" fill="none" stroke="var(--charcoal)" stroke-width="1.1"/><path d="M4 8h8M8 4c-2 2.4-2 5.6 0 8M8 4c2 2.4 2 5.6 0 8" fill="none" stroke="var(--charcoal)" stroke-width="1"/></svg>
        <span>www.lomvex.com.au</span>
      </li>
    </ul>

    <div class="card-holder">
      <p class="holder-name">Daniel Reyes</p>
      <p class="holder-role">Owner / C.E.O</p>
    </div>
  </div>
</body>
</html>
```